Business card design needed for Renewable utilities company based in New Zealand.

We supply and install solar panels and all components along with it for a fully customisable PV system that helps customer save money on their energy bills right away and also save the planet!

I have attached logo & website design files to give you a better insight.

Industry/Entity Type

Business

```html
<!DOCTYPE html>
<html lang="en">
<head>
<meta charset="utf-8">
<title>Sunfield Power – Business Card</title>
<link rel="stylesheet" href="https://fonts.googleapis.com/css2?family=Questrial&family=Marcellus+SC&display=swap">
<style>
  :root{
    --backdrop:#d9dadc;
    --navy-light:#2f5591;
    --navy-dark:#0d2148;
    --map-tone:rgba(160,190,230,0.18);
    --white:#ffffff;
    --brand-blue:#1c68c4;
    --ink:#3a3a3a;
    --title-blue:#1f4fa8;
    --icon-blue:#1f4fa8;
  }
  *{margin:0;padding:0;box-sizing:border-box}
  html,body{width:1200px;height:871px;overflow:hidden;background:var(--backdrop)}
  .canvas{position:relative;width:1200px;height:871px}

  .card{position:absolute;width:560px;height:320px;border-radius:2px;box-shadow:0 10px 30px rgba(0,0,0,.25)}

  /* Front */
  .card-front{left:120px;top:90px;background:linear-gradient(160deg,var(--navy-light),var(--navy-dark));overflow:hidden}
  .world-map{position:absolute;left:40px;top:40px;width:480px;height:240px;border-radius:40% 45% 35% 50%;background:radial-gradient(ellipse at center,var(--map-tone),transparent 70%)}
  .front-brand{position:absolute;left:0;right:0;top:92px;text-align:center}
  .front-brand .brand-dot{display:block;margin:0 auto 18px;width:74px;height:74px;border-radius:50%;background:var(--white)}
  .front-brand .brand-name{font-family:'Questrial',sans-serif;font-size:38px;color:var(--white);letter-spacing:.5px}

  /* Back */
  .card-back{left:520px;top:450px;background:var(--white)}
  .back-brand{position:absolute;left:34px;top:92px;width:210px;text-align:center}
  .back-brand .brand-dot{display:block;margin:0 auto 14px;width:70px;height:70px;border-radius:50%;background:var(--brand-blue)}
  .back-brand .brand-name{font-family:'Questrial',sans-serif;font-size:28px;color:var(--brand-blue)}

  .contact{position:absolute;left:290px;top:62px;font-family:'Questrial',sans-serif;color:var(--ink)}
  .contact .person-name{font-family:'Marcellus SC',serif;font-size:18px;letter-spacing:1.5px;color:var(--ink)}
  .contact .person-title{font-family:'Marcellus SC',serif;font-size:13px;letter-spacing:1px;color:var(--title-blue);margin-bottom:22px}
  .contact .address{font-size:13px;line-height:17px;margin-bottom:20px}
  .contact ul{list-style:none}
  .contact li{display:flex;align-items:center;font-size:13px;line-height:19px}
  .contact li svg{width:11px;height:11px;margin-right:14px;fill:var(--icon-blue)}
</style>
</head>
<body>
<div class="canvas">

  <section class="card card-front">
    <div class="world-map" role="img" aria-label="Faint dotted world map in light blue"></div>
    <div class="front-brand">
      <span class="brand-dot"></span>
      <span class="brand-name">Sunfield Power</span>
    </div>
  </section>

  <section class="card card-back">
    <div class="back-brand">
      <span class="brand-dot"></span>
      <span class="brand-name">Sunfield Power</span>
    </div>

    <div class="contact">
      <p class="person-name">Daniel R. Whitford</p>
      <p class="person-title">Instructur</p>
      <p class="address">48 Harbour View Rd. Unit 3<br>Tauranga, NZ 3110</p>
      <ul>
        <li>
          <svg viewBox="0 0 12 12" aria-hidden="true"><path d="M2 1h3l1 3-1.5 1a6 6 0 0 0 2.5 2.5L8 6l3 1v3a1 1 0 0 1-1 1A9 9 0 0 1 1 2a1 1 0 0 1 1-1z"/></svg>
          555-201-4417
        </li>
        <li>
          <svg viewBox="0 0 12 12" aria-hidden="true"><rect x="3" y="1" width="6" height="3"/><rect x="1" y="4.5" width="10" height="5" rx="1"/><rect x="3" y="8" width="6" height="3"/></svg>
          555-201-4418
        </li>
        <li>
          <svg viewBox="0 0 12 12" aria-hidden="true"><path d="M1 2.5h10v7H1z M1 2.5l5 4 5-4" fill="none" stroke="#1f4fa8" stroke-width="1.2"/></svg>
          daniel@sunfieldpower.com
        </li>
        <li>
          <svg viewBox="0 0 12 12" aria-hidden="true"><circle cx="6" cy="6" r="4.8" fill="none" stroke="#1f4fa8" stroke-width="1.2"/><path d="M1.2 6h9.6M6 1.2c-2.5 3-2.5 6.6 0 9.6M6 1.2c2.5 3 2.5 6.6 0 9.6" fill="none" stroke="#1f4fa8" stroke-width=".9"/></svg>
          www.sunfieldpower.com
        </li>
      </ul>
    </div>
  </section>

</div>
</body>
</html>
```